Premium Lawn fertiliser packaging - Looking for long term designer

*Update at bottom
I need a carefully considered, bold and professional packaging design for my new premium lawn fertiliser product. This contest is for a detailed front of the stand-up pouch packaging and once I’ve chosen a winner, they’ll be asked to create the layout for the back that links to the front as well. I have a full range of additional products that will also need designs and so I'm looking for someone who can do a great job here and who we can work with long term.

The front should include our logo for Pemberly Turf Supply Direct and be titled “Bloom Vigor Max” "Professional Lawn Fertiliser". The spring fertiliser tag line is "Awaken your lawn: Lush Greening, Lasting Health".
Beneath it, it then needs to include some important usage information and the key benefits along with some suitable graphic.

Key information to include:

Apply March - June
Treats 35-50 m2
16-3-8
+2%MgO + 1% Fe + 2.9% CaO (this is the chemical makeup of the fertiliser and needs to be fairly prominent. If you look at other professional fertiliser packaging, you'll see how it needs to compare).

Key features:
Premium fertiliser, used by professionals
Advanced greening with micro-nutrient complex
Dual action Nitrogen: Instant green boost & continuous feed for 3 months
Child & pet safe

Our brand colours are purple and green. Purple = #592999, Green = 3cb64a / 81d742 / 4d9d44

I think these colours look great against a white background.

Please make sure you look at our website as well to get an idea of our brand: www.pemberlyturfsupply.co.uk

To help, I've attached images of competitors fertiliser packaging that I like the look of. I'm not looking for you to copy but just see what type of thing appeals to me, the standard I'm expecting and what I need to compete against....

In addition, I have also attached some potential images you may wish to try using in your design, although please feel free to use your own if you have something better. For the moment, the images are 'preview' images, but once I decide on a design and we agree on the correct image, I will download and send over a fully licensed version.

*** Update*** When submitting your design, can you submit it in 2 formats: The first as a fully printed custom stand-up pouch and the second as a full-size label stuck onto a standup pouch (whatever colour you think is right for your design - choose white if you are not sure). To explain, I've just discovered we won't be able to get full custom bags printed in time for the first run and so we will have to opt for the design to be printed on labels and fixed onto bags. I therefore need to choose a design that works in both formats as both a label on a standup pouch as well as a fully printed pouch. Many thanks.

Target Market(s)

Domestic home-owners

Industry/Entity Type

Lawn care. NOT AGRICULTURE OR FARMING

Font styles to use
Sans Serif

Requirements
Must have
• Presented in 2 formats - see update at bottom of description
Nice to have
• I quite like designs against a white background, although I’m open to other ideas as well.
Should not have
• Please do not include any people or faces in the design. The text should be solid in colour, so no graduated colour fill in the text or outline text. Please avoid over-busy or cluttered designs.

```html
<!DOCTYPE html>
<html lang="en">
<head>
<meta charset="UTF-8">
<title>Bloom Vigor Max – Professional Lawn Fertiliser Label</title>
<link rel="stylesheet" href="https://fonts.googleapis.com/css2?family=Anton&family=Righteous&family=Poppins:wght@300;400;600;700&display=swap">
<style>
  :root {
    --stage: #687f4f;
    --white: #ffffff;
    --brand-green: #4d9d44;
    --title-green: #3cb64a;
    --lime: #81d742;
    --deep-green: #1f4f1c;
    --grass-mid: #3f7f2a;
    --brown: #3a2820;
    --ink: #2b2b2b;
    --divider: #d6d6d6;
  }
  * { margin: 0; padding: 0; box-sizing: border-box; }
  html, body { width: 1200px; height: 2400px; overflow: hidden; }
  body { background: var(--stage); position: relative; font-family: "Poppins", sans-serif; }

  .label {
    position: absolute; left: 60px; top: 285px;
    width: 1080px; height: 1830px;
    background: var(--white);
    overflow: hidden;
    box-shadow: 0 20px 50px rgba(0,0,0,.35);
  }
  .label-art { position: absolute; inset: 0; width: 1080px; height: 1830px; }

  .brand-seal {
    position: absolute; left: 320px; top: 230px;
    width: 440px; height: 440px; border-radius: 50%;
    display: flex; align-items: center; justify-content: center;
    text-align: center;
  }
  .brand-name {
    font-family: "Poppins", sans-serif; font-weight: 600;
    font-size: 46px; line-height: 1.15; color: var(--brown);
    width: 330px;
  }

  .centered { position: absolute; left: 0; width: 100%; text-align: center; }
  .product-title {
    top: 655px; font-family: "Anton", sans-serif; font-size: 132px;
    line-height: 1; color: var(--title-green); letter-spacing: 1px;
  }
  .product-kind {
    top: 808px; font-family: "Righteous", sans-serif; font-size: 66px;
    line-height: 1; color: var(--brown); letter-spacing: 3px;
  }
  .product-type {
    position: absolute; left: 140px; top: 889px; width: 821px; height: 78px;
    background: var(--brown); color: var(--white);
    font-family: "Righteous", sans-serif; font-size: 62px; letter-spacing: 8px;
    display: flex; align-items: center; justify-content: center;
  }
  .tagline-main {
    top: 988px; font-weight: 300; font-size: 48px; letter-spacing: 8px; color: var(--ink);
  }
  .tagline-sub {
    top: 1040px; font-weight: 400; font-size: 38px; letter-spacing: 7px; color: var(--brand-green);
  }

  .feature {
    position: absolute; top: 1120px; width: 310px; text-align: center;
    font-size: 25px; line-height: 1.15; color: var(--ink);
  }
  .feature strong { font-weight: 700; display: block; }
  .feature svg { display: block; margin: 0 auto 14px; }
  .feature-one { left: 54px; }
  .feature-two { left: 367px; }
  .feature-three { left: 697px; }
  .feature-rule {
    position: absolute; top: 1085px; width: 2px; height: 275px;
    background: linear-gradient(var(--divider), rgba(214,214,214,0));
  }

  .safety-badge { position: absolute; left: 140px; top: 1478px; }
  .usage-window {
    position: absolute; left: 322px; top: 1530px;
    font-family: "Righteous", sans-serif; font-size: 48px; color: var(--white); letter-spacing: 2px;
  }
  .analysis-bar {
    position: absolute; left: 277px; top: 1594px; width: 684px; height: 50px;
    background: var(--white); color: var(--brown);
    font-family: "Righteous", sans-serif; font-size: 40px; letter-spacing: 2px;
    display: flex; align-items: center; justify-content: center;
  }
  .usage-facts {
    top: 1658px; font-size: 34px; color: var(--white); padding-left: 60px;
  }
  .usage-facts .tick { color: var(--lime); font-weight: 700; margin-right: 4px; }
  .usage-facts .gap { display: inline-block; width: 44px; }
  .pack-size {
    top: 1722px; font-size: 30px; color: var(--lime); padding-left: 10px;
  }
  .pack-size b { color: var(--white); font-weight: 700; font-size: 40px; }
  .pack-size small { color: var(--white); font-weight: 700; font-size: 28px; }
</style>
</head>
<body>
  <main class="label">
    <svg class="label-art" viewBox="0 0 1080 1830" xmlns="http://www.w3.org/2000/svg">
      <defs>
        <linearGradient id="lawnPhoto" x1="0" y1="0" x2="0" y2="1">
          <stop offset="0" stop-color="#6e8a5a"/>
          <stop offset="0.25" stop-color="#9fc25a"/>
          <stop offset="0.6" stop-color="#6aa52a"/>
          <stop offset="1" stop-color="#2f6a1a"/>
        </linearGradient>
        <linearGradient id="grassBand" x1="0" y1="0" x2="0" y2="1">
          <stop offset="0" stop-color="#ffffff" stop-opacity="0"/>
          <stop offset="0.12" stop-color="#5f9a36"/>
          <stop offset="0.35" stop-color="#2e6a22"/>
          <stop offset="1" stop-color="#1f4f1c"/>
        </linearGradient>
      </defs>
      <rect role="img" aria-label="Close-up photo of a lush green lawn with a house blurred in the background" x="0" y="0" width="1080" height="520" fill="url(#lawnPhoto)"/>
      <path d="M0 360 Q330 480 540 480 Q750 480 1080 360 L1080 1830 L0 1830 Z" fill="#ffffff"/>
      <path d="M35 330 Q200 440 345 452 Q200 470 35 330 Z" fill="#3a2820"/>
      <path d="M1045 330 Q880 440 735 452 Q880 470 1045 330 Z" fill="#3a2820"/>
      <circle cx="540" cy="450" r="220" fill="#ffffff" stroke="#3a2820" stroke-width="7"/>
      <rect role="img" aria-label="Photo of tall green grass blades rising into a dark green band" x="0" y="1330" width="1080" height="500" fill="url(#grassBand)"/>
    </svg>

    <div class="brand-seal">
      <p class="brand-name">Pemberly Turf Supply Direct</p>
    </div>

    <h1 class="centered product-title">BLOOM VIGOR MAX</h1>
    <p class="centered product-kind">PROFESSIONAL</p>
    <p class="product-type">LAWN FERTILISER</p>
    <p class="centered tagline-main">AWAKEN YOUR LAWN</p>
    <p class="centered tagline-sub">LUSH GREENING, LASTING HEALTH</p>

    <div class="feature feature-one">
      <svg width="84" height="84" viewBox="0 0 84 84"><circle cx="42" cy="42" r="40" fill="#4d9d44"/><path d="M26 36 L32 27 H52 L58 36 L42 58 Z M26 36 H58 M36 27 L42 36 L48 27 M42 36 V58" fill="none" stroke="#fff" stroke-width="2.5" stroke-linejoin="round"/></svg>
      <strong>Premium fertiliser</strong>used by professionals
    </div>
    <span class="feature-rule" style="left:359px"></span>
    <div class="feature feature-two">
      <svg width="84" height="84" viewBox="0 0 84 84"><circle cx="42" cy="42" r="40" fill="#4d9d44"/><path d="M24 58 H60 M30 58 Q28 42 22 34 M36 58 Q36 40 32 28 M42 58 Q43 38 48 26 M48 58 Q50 44 58 36 M54 58 Q56 50 62 46" fill="none" stroke="#fff" stroke-width="2.5" stroke-linecap="round"/></svg>
      <strong>Advanced greening</strong>with micro-nutrient complex
    </div>
    <span class="feature-rule" style="left:682px"></span>
    <div class="feature feature-three">
      <svg width="84" height="84" viewBox="0 0 84 84"><circle cx="42" cy="42" r="40" fill="#4d9d44"/><path d="M42 46 V30 M42 34 Q34 24 28 28 Q32 36 42 34 M42 32 Q50 20 56 24 Q52 32 42 32 M24 50 Q34 46 44 52 L58 48 Q62 48 60 52 L46 60 H24" fill="none" stroke="#fff" stroke-width="2.5" stroke-linecap="round" stroke-linejoin="round"/></svg>
      <strong>Dual action Nitrogen:</strong>Instant green boost &amp; continuous feed for 3 months
    </div>

    <svg class="safety-badge" width="156" height="162" viewBox="0 0 156 162">
      <path d="M78 4 L150 26 V80 Q150 132 78 158 Q6 132 6 80 V26 Z" fill="#4d9d44" stroke="#ffffff" stroke-width="5"/>
      <text x="78" y="112" text-anchor="middle" font-family="Poppins, sans-serif" font-weight="700" font-size="17" fill="#1f4f1c">CHILD &amp; PET</text>
      <text x="78" y="132" text-anchor="middle" font-family="Poppins, sans-serif" font-weight="700" font-size="17" fill="#1f4f1c">SAFE</text>
    </svg>
    <p class="usage-window">APPLY MARCH - JUNE</p>
    <p class="analysis-bar">+2%MGO + 1% FE + 2.9% CAO</p>
    <p class="centered usage-facts"><span class="tick">✓</span>Treats 35-50 m2<span class="gap"></span><span class="tick">✓</span>16-3-8</p>
    <p class="centered pack-size">NETWT. <b>10</b><small>LBS</small> &nbsp; COVERS UP TO <b>2500</b><small>SQFT.</small></p>
  </main>
</body>
</html>
```